2023 Crestline Group Brochure design

We need help with the visual on our packages. Please see https://www.vidmarrow.com/share/4f71c2ab90de58b3e6a1d2c7f0b94e18

We are looking for a really creative way to highlight our packages. This is the main thing we are wanting to aesthetically different. We will select the best design that looks the best for the customer to easily be able to see the difference between the packages etc.

Target Market(s)

Real Estate Agents and Buyers

Requirements
Must have
• NEW Package Layout that makes it easy for the customer to see the packages Crestline Core and Crestline Prime. Must keep Brand design and colors etc.

```html
<!DOCTYPE html>
<html lang="en">
<head>
<meta charset="utf-8">
<title>Crestline Group Brochure – Inside</title>
<link href="https://fonts.googleapis.com/css2?family=Montserrat:wght@400;500;600;700;800&display=swap" rel="stylesheet">
<style>
:root{
  --stage:#c9c9c9;
  --navy:#0d2b57;
  --navy-deep:#0a2348;
  --royal:#1559a6;
  --sky:#1d8fe8;
  --column-core:#1670c8;
  --column-prime:#1a80d8;
  --accent:#2fa3f2;
  --mist:#e2e4e7;
  --white:#ffffff;
  --ink:#1c2230;
}
*{box-sizing:border-box;margin:0;padding:0}
html,body{width:1200px;height:900px;overflow:hidden}
body{background:var(--stage);font-family:"Montserrat",Arial,sans-serif;color:var(--ink);position:relative}
.brochure{position:absolute;left:110px;top:35px;width:960px;height:743px;background:var(--white);overflow:hidden}
.top-band{position:absolute;left:0;top:0;width:640px;height:55px;background:var(--mist)}
.packages-title{position:absolute;left:0;top:25px;width:640px;text-align:center;font-size:14.5px;font-weight:700;color:var(--navy);letter-spacing:.2px}

/* Panel 1 */
.tab-core{position:absolute;left:45px;top:55px;width:230px;height:47px;background:linear-gradient(90deg,var(--navy),var(--royal));border-radius:0 0 24px 24px;color:var(--white);display:flex;align-items:center;padding-left:30px;gap:8px}
.tab-num{font-size:26px;font-weight:800}
.tab-name{font-size:14.5px;font-weight:700;line-height:1.2}
.feature{position:absolute;left:0;width:288px;text-align:center;font-size:9.6px;line-height:1.3;color:var(--ink)}
.feature h4{font-size:9.6px;font-weight:700;color:var(--navy);margin-top:3px}
.feature-icon{width:30px;height:30px;margin:0 auto;border-radius:7px;background:var(--navy)}
.feature-icon.round{border-radius:50%}
.benefits{position:absolute;left:0;top:485px;width:286px;height:258px;background:linear-gradient(180deg,var(--navy) 0%,var(--royal) 100%);border-radius:0 30px 0 0;color:var(--white);padding:18px 0 0 30px}
.benefits h3{font-size:14px;font-weight:700;margin-bottom:18px}
.benefit{display:flex;gap:14px;margin-bottom:16px}
.benefit-icon{flex:none;width:30px;height:24px;background:var(--accent);border-radius:4px;margin-top:4px}
.benefit h5{font-size:9.4px;font-weight:700;color:var(--accent);line-height:1.2}
.benefit p{font-size:9.6px;line-height:1.3;width:185px}

/* Panel 2 */
.prime-card{position:absolute;left:304px;top:48px;width:314px;height:642px;background:linear-gradient(180deg,var(--navy-deep) 0%,var(--royal) 100%);border-radius:34px 34px 0 70px;color:var(--white);text-align:center}
.prime-head{display:flex;align-items:center;justify-content:center;gap:8px;padding-top:12px}
.prime-head .tab-num{font-size:28px}
.prime-head .tab-name{font-size:14.5px;text-align:left}
.prime-rule{width:254px;height:1px;background:rgba(255,255,255,.6);margin:6px auto 0}
.prime-note{font-size:8.5px;font-style:italic;margin-top:6px;opacity:.9}
.perk{margin:0 auto;width:290px;font-size:9.6px;line-height:1.3}
.perk h4{font-size:9.2px;font-weight:700;color:var(--accent);margin-top:2px}
.perk-icon{width:26px;height:26px;border-radius:50%;background:var(--white);margin:10px auto 2px}
.perk-badge{width:84px;height:16px;border-radius:3px;background:rgba(255,255,255,.85);margin:10px auto 2px}
.footnote{position:absolute;left:304px;top:698px;width:314px;text-align:center;font-size:8.3px;font-weight:600;line-height:1.35;color:var(--navy)}

/* Panel 3 */
.compare{position:absolute;left:640px;top:0;width:320px;height:743px;background:var(--sky)}
.compare svg{position:absolute;left:0;top:0}
.compare-title{position:absolute;left:22px;top:52px;display:flex;align-items:center;gap:8px;color:var(--navy)}
.compare-title b{font-size:38px;font-weight:800}
.compare-title span{font-size:14.5px;font-weight:800;line-height:1.2}
.col-label{position:absolute;font-size:10.5px;font-weight:700;color:var(--navy);line-height:1.15;writing-mode:vertical-rl;transform:rotate(180deg)}
.rows{position:absolute;left:0;top:0;width:320px}
.row{position:absolute;left:14px;width:286px;display:flex;align-items:flex-start;font-size:9.2px;line-height:1.25;color:var(--navy);font-weight:500}
.row .tick{width:14px;flex:none;margin-right:6px;font-weight:700}
.row .label{width:140px}
.row::after{content:"";position:absolute;left:0;right:0;bottom:-5px;height:1px;background:rgba(13,43,87,.15)}
.dot{position:absolute;width:12px;height:12px;border-radius:50%;border:1.5px solid var(--navy);background:rgba(255,255,255,.15)}
.payment{position:absolute;left:0;top:585px;width:320px;text-align:center;color:var(--white);font-size:18px;font-weight:800;line-height:1.35}
.brand-mark{position:absolute;left:0;top:670px;width:320px;display:flex;align-items:center;justify-content:center;gap:7px;color:var(--white);font-size:11px;font-weight:700}
.brand-mark i{width:16px;height:16px;border-radius:50%;border:2px solid var(--navy)}
</style>
</head>
<body>
<main class="brochure">
  <div class="top-band"></div>
  <h2 class="packages-title">CHOOSE BETWEEN OUR INSPECTION PACKAGES</h2>

  <!-- Panel 1: Core package -->
  <div class="tab-core"><span class="tab-num">1.</span><span class="tab-name">Crestline Core<br>Home Inspection</span></div>

  <section class="feature" style="top:113px"><div class="feature-icon" role="img" aria-label="Inspector icon"></div><h4>CERTIFIED INSPECTORS</h4><p>Our inspectors are background checked and<br>verified to have insurance.</p></section>
  <section class="feature" style="top:188px"><div class="feature-icon round" role="img" aria-label="Magnifying glass icon"></div><h4>COMPREHENSIVE INSPECTION REPORT</h4><p>A professional, digital-format inspection report,<br>complete with detailed photos and a summary page<br>– all delivered within 24 hours of the inspection.</p></section>
  <section class="feature" style="top:278px"><div class="feature-icon" role="img" aria-label="Inspection checklist icon"></div><h4>IN-DEPTH INSPECTION</h4><p>Over 1,800 items in the house are checked during a<br>Crestline inspection, including the plumbing, heating, air<br>conditioning, and electrical systems, the foundation,<br>structure, roof, and property grounds.</p></section>
  <section class="feature" style="top:380px"><div class="feature-icon" role="img" aria-label="Infrared scanner icon"></div><h4>WHOLE-HOUSE INFRARED SCANS</h4><p>Extensive infrared scans help us detect air duct<br>leakage, electrical hotspots, and hidden moisture – all<br>problems that are not apparent to the naked eye.</p></section>

  <section class="benefits">
    <h3>BENEFITS INCLUDE</h3>
    <div class="benefit"><span class="benefit-icon"></span><div><h5>MAINTENANCE REMINDER<br>EMAIL ALERTS</h5><p>Automated alerts reminding you to change batteries, filters, and more!</p></div></div>
    <div class="benefit"><span class="benefit-icon"></span><div><h5>DOCUMENT AND PHOTO<br>STORAGE</h5><p>A Storage location for all of your home-related documents and photos</p></div></div>
    <div class="benefit"><span class="benefit-icon"></span><div><h5>APPLIANCE RECALL ALERTS</h5><p>Automated emails to alert you in the event of a recall on one of your appliances.</p></div></div>
  </section>

  <!-- Panel 2: Prime package -->
  <section class="prime-card">
    <div class="prime-head"><span class="tab-num">2.</span><span class="tab-name">Crestline Prime Home<br>Inspection</span></div>
    <div class="prime-rule"></div>
    <p class="prime-note">(Includes everything in the basic inspection, plus the following)</p>

    <div class="perk"><div class="perk-icon" role="img" aria-label="Repair pricing icon"></div><h4>REQUEST FOR REPAIR PRICER</h4><p>Turn your Crestline home inspection report summary into an estimate of repairs &amp; receive your pricing report within 24 hours of receiving your Home Inspection report. (This report is optional and emailed to the agent only- excludes pools and sewer lines)</p></div>
    <div class="perk"><div class="perk-icon" role="img" aria-label="Warranty seal icon"></div><h4>90 DAY WARRANTY</h4><p>Covers the home for Mechanical and Structural items that were confirmed to be working at the time of inspection.</p></div>
    <div class="perk"><div class="perk-badge" role="img" aria-label="Roof protection plan partner badge"></div><h4>SUMMIT ROOF PROTECTION PLAN</h4><p>The Summit Roof Protection Plan provides 5 years of coverage and protection for roof leak failures due to normal wear and tear or deterioration. This policy covers all residential roof types.</p></div>
    <div class="perk"><div class="perk-badge" role="img" aria-label="Mold coverage partner badge"></div><h4>DAMP COVER</h4><p>Our mold agreement provides coverage for visible mold on surfaces permanently installed in the subject's property. In order to receive coverage there must be no record of mold or moisture issues at the time of the inspection.</p></div>
    <div class="perk"><div class="perk-badge" role="img" aria-label="Sewer line guarantee partner badge"></div><h4>PIPE SURE</h4><p>The Crestline 90-Day Underground Sewer/Water Line Guarantee gives you assurance that the underground sewer/water line are covered from the street to the house. *Not an inspection.</p></div>
    <div class="perk"><div class="perk-icon" role="img" aria-label="Sprinkler icon"></div><h4>SPRINKLER &amp; IRRIGATION INSPECTION</h4><p>One control box and inspection of visible sprinkler heads. (Additional control boxes are $30 each) *exterior landscaping sprinkler systems only. Fire sprinklers are not inspected.</p></div>
  </section>
  <p class="footnote">* for more information on warranties see<br>www.crestlineinspect.com/warranty-guide</p>

  <!-- Panel 3: comparison -->
  <section class="compare">
    <svg width="320" height="743" viewBox="0 0 320 743" aria-hidden="true">
      <path d="M235 0 H300 V555 H275 Q235 555 235 515 Z" fill="var(--column-prime)"/>
      <path d="M235 0 H300 V143 H275 Q235 143 235 103 Z" fill="var(--mist)"/>
      <path d="M165 0 H235 V485 Q235 525 195 525 H165 Z" fill="var(--column-core)"/>
      <path d="M165 0 H235 V135 H205 Q165 135 165 95 Z" fill="var(--mist)"/>
      <path d="M0 0 H165 V100 Q165 135 130 135 H0 Z" fill="var(--mist)"/>
    </svg>
    <div class="compare-title"><b>2</b><span>SERVICE<br>PACKAGES</span></div>
    <div class="col-label" style="left:183px;top:24px;height:100px">Crestline Core<br>Inspection</div>
    <div class="col-label" style="left:253px;top:24px;height:100px">Crestline Prime<br>Inspection</div>

    <div class="rows">
      <div class="row" style="top:160px"><span class="tick">✓</span><span class="label">Certified Professional Inspector</span></div>
      <div class="row" style="top:191px"><span class="tick">✓</span><span class="label">Infrared Scan ($250 value)</span></div>
      <div class="row" style="top:212px"><span class="tick">✓</span><span class="label">1,800+ Item Evaluation</span></div>
      <div class="row" style="top:233px"><span class="tick">✓</span><span class="label">Professional and Digital Photo Report with Summary Page</span></div>
      <div class="row" style="top:276px"><span class="tick">✓</span><span class="label">Exceptional Customer Service Assistance &amp; Scheduling</span></div>
      <div class="row" style="top:320px"><span class="tick">✓</span><span class="label">100 Day Guarantee</span></div>
      <div class="row" style="top:340px"><span class="tick">✓</span><span class="label">Request for Repairs Pricer</span></div>
      <div class="row" style="top:360px"><span class="tick">✓</span><span class="label">PipeSure</span></div>
      <div class="row" style="top:381px"><span class="tick">✓</span><span class="label">DampCover</span></div>
      <div class="row" style="top:402px"><span class="tick">✓</span><span class="label">5 Year Summit Roof Warranty</span></div>
      <div class="row" style="top:435px"><span class="tick">✓</span><span class="label">Sprinkler and Irrigation Inspection</span></div>
      <div class="row" style="top:470px"><span class="tick">✓</span><span class="label">90-Day Warranty</span></div>
      <div class="row" style="top:494px"><span class="tick">✓</span><span class="label">Home Safety PDF</span></div>

      <span class="dot" style="left:194px;top:163px"></span>
      <span class="dot" style="left:194px;top:191px"></span>
      <span class="dot" style="left:194px;top:212px"></span>
      <span class="dot" style="left:194px;top:243px"></span>
      <span class="dot" style="left:194px;top:286px"></span>
      <span class="dot" style="left:194px;top:320px"></span>
      <span class="dot" style="left:262px;top:163px"></span>
      <span class="dot" style="left:262px;top:191px"></span>
      <span class="dot" style="left:262px;top:212px"></span>
      <span class="dot" style="left:262px;top:243px"></span>
      <span class="dot" style="left:262px;top:286px"></span>
      <span class="dot" style="left:262px;top:320px"></span>
      <span class="dot" style="left:262px;top:340px"></span>
      <span class="dot" style="left:262px;top:360px"></span>
      <span class="dot" style="left:262px;top:381px"></span>
      <span class="dot" style="left:262px;top:405px"></span>
      <span class="dot" style="left:262px;top:438px"></span>
      <span class="dot" style="left:262px;top:470px"></span>
      <span class="dot" style="left:262px;top:494px"></span>
    </div>

    <p class="payment">PAYMENT AT<br>CLOSE OF ESCROW<br>AVAILABLE.</p>
    <div class="brand-mark"><i></i>Crestline Group</div>
  </section>
</main>
</body>
</html>
```